The label Velomira Dijon Mustard

Hello everybody,
What we need : a design for a label of Dijon Mustard it's a new project and. What we're looking for : a european style with a warm vibe. The product's target : the North American.

The design must be elegant, modern and up market.don't hesitate to think outside the box.
we attached a file contain our logo. the logo for this product will be the main logo the third one.
and we attached a sizes and the inspiration design BRUNEL and SORVEN

Target Market(s)

North America

Logo Text

Velomira

Logo styles of interest
Wordmark Logo
Font styles to use
Serif
Script

Colors

Designer to choose colors to be used in the design.

Requirements
Must have
• -The brand ''Velomira'' and the logo is (the Main logo The Third one) attached file.
• - the name of the product, ''Dijon Mustard /Moutarde de Dijon/ ديجون الخردل'', in English, French and Arabic
• -The Lid will be red or black depend of your design.
• - the nutrition fact. Make a place and it will be changed by us.
• -Ingrediants:
• fr: eau, graines de MOUTARDE, vinaigre d'alcool, sel, acidifiant : acide citrique, conservateur : E224 (SULFITES).
• En: water, MUSTARD seeds, alcohol vinegar, salt, acidifier: citric acid, preservative: E224 (SULFITES).
• Ar: ماء ، بذور الخردل ، خل الكحول ، الملح ، محمض: حمض الستريك ، مواد حافظة: E224
• - the weight of 295g/ 250ml
• - conditioned by Sarl Velomira/conditionné par Sarl Velomira.
• -Slogan In French''Apportez le vrai goût à votre maison''
• -design must be elegant, modern and up market.
Nice to have
• -A minimalist design style
• -Design color: red or black.

```html
<!DOCTYPE html>
<html lang="en">
<head>
<meta charset="utf-8">
<title>Velomira Dijon Mustard – Label</title>
<link rel="stylesheet" href="https://fonts.googleapis.com/css2?family=Libre+Caslon+Text:wght@400;700&family=Great+Vibes&family=Noto+Naskh+Arabic:wght@400&family=Jost:wght@400&display=swap">
<style>
  :root {
    --page: #ffffff;
    --frame-dark: #3b403b;
    --cream: #f3ecdb;
    --gold-line: #e2c15a;
    --rule-grey: #8a8a84;
    --brand-green: #1f5b40;
    --accent-red: #d63b2e;
    --ink: #3c3c38;
    --caption: #4a4a46;
  }
  html, body {
    margin: 0;
    padding: 0;
    width: 1200px;
    height: 1200px;
    overflow: hidden;
    background: var(--page);
  }
  .canvas {
    position: relative;
    width: 1200px;
    height: 1200px;
  }
  .label {
    position: absolute;
    top: 330px;
    width: 525px;
    height: 528px;
  }
  .label--front { left: 50px; }
  .label--back { left: 625px; }
  .caption {
    position: absolute;
    top: 895px;
    width: 525px;
    text-align: center;
    font-family: "Libre Caslon Text", serif;
    font-size: 15px;
    letter-spacing: 0.3em;
    color: var(--caption);
  }
  .caption--front { left: 50px; }
  .caption--back { left: 625px; }

  .serif { font-family: "Libre Caslon Text", serif; }
  .script { font-family: "Great Vibes", cursive; }
  .arabic { font-family: "Noto Naskh Arabic", serif; }
  .sans { font-family: "Jost", sans-serif; }

  .frame-outer { fill: var(--frame-dark); }
  .frame-fill { fill: var(--cream); }
  .frame-gold { fill: none; stroke: var(--gold-line); stroke-width: 0.9; }
  .frame-inner { fill: none; stroke: var(--rule-grey); stroke-width: 0.5; }
  .band { fill: var(--frame-dark); }
  .brand-name { fill: var(--brand-green); font-weight: 700; }
  .brand-dot { fill: var(--brand-green); }
  .product-script { fill: var(--cream); }
  .red { fill: var(--accent-red); }
  .ink { fill: var(--ink); }
  .rule { stroke: var(--rule-grey); stroke-width: 0.5; }
  .nf-box { fill: none; stroke: #1e1e1e; stroke-width: 1; }
  .nf-rule { stroke: #1e1e1e; stroke-width: 0.5; }
  .nf-rule--thick { stroke: #1e1e1e; stroke-width: 1.6; }
  .nf-text { fill: #1e1e1e; }
</style>
</head>
<body>
<main class="canvas">

  <!-- Front label -->
  <svg class="label label--front" viewBox="0 0 328 330" aria-label="Front label">
    <path class="frame-outer" d="M0,18 H68 Q78,18 81,9 Q84,0 96,0 H232 Q244,0 247,9 Q250,18 260,18 H328 V330 H0 Z"/>
    <path class="frame-fill" d="M7,25 H72 Q83,25 87,15 Q90,7 100,7 H228 Q238,7 241,15 Q245,25 256,25 H321 V323 H7 Z"/>
    <path class="frame-gold" d="M11,29 H74 Q86,29 90,18 Q93,11 102,11 H226 Q235,11 238,18 Q242,29 254,29 H317 V319 H11 Z"/>
    <path class="frame-inner" d="M21,40 H78 Q90,40 94,28 Q97,21 106,21 H222 Q231,21 234,28 Q238,40 250,40 H307 V309 H21 Z"/>

    <text class="serif brand-name" x="155" y="96" font-size="34" text-anchor="middle">Velomira</text>
    <circle class="brand-dot" cx="245" cy="82" r="4"/>

    <polygon class="band" points="-3,190 330,112 330,162 -3,240"/>
    <text class="script product-script" x="164" y="186" font-size="28" text-anchor="middle" transform="rotate(-13 164 178)">Moutarde de Dijon</text>

    <text class="serif red" x="164" y="236" font-size="9" letter-spacing="1.4" text-anchor="middle">DIJON MUSTARD</text>
    <line class="rule" x1="88" y1="243" x2="242" y2="243"/>
    <text class="arabic red" x="164" y="259" font-size="10" text-anchor="middle" direction="rtl">ديجون الخردل</text>

    <text class="serif ink" x="164" y="306" font-size="6" text-anchor="middle">295g/ 250ml</text>
  </svg>

  <!-- Back label -->
  <svg class="label label--back" viewBox="0 0 328 330" aria-label="Back label">
    <rect class="frame-outer" x="0" y="0" width="328" height="330"/>
    <rect class="frame-fill" x="7" y="7" width="314" height="316"/>
    <rect class="frame-gold" x="11" y="11" width="306" height="308"/>
    <rect class="frame-inner" x="21" y="21" width="286" height="288"/>

    <g class="serif red" font-size="8" letter-spacing="0.9">
      <text x="42" y="56">APPORTEZ LE</text>
      <text x="42" y="68">VRAI GOÛT</text>
      <text x="42" y="80">À VOTRE MAISON</text>
    </g>
    <line class="rule" x1="42" y1="97" x2="160" y2="97"/>
    <text class="serif ink" x="42" y="113" font-size="6.5" letter-spacing="1.6">INGREDIENTS</text>
    <line class="rule" x1="42" y1="121" x2="160" y2="121"/>

    <g class="serif ink" font-size="4.6">
      <text x="42" y="139">Fr: Eau, Graines De Moutarde,</text>
      <text x="42" y="147">Vinaigre D'alcool, Sel, Acidifiant :</text>
      <text x="42" y="155">Acide Citrique, Conservateur : E224</text>
      <text x="42" y="163">(Sulfites).</text>
    </g>
    <line class="rule" x1="42" y1="180" x2="160" y2="180"/>
    <g class="serif ink" font-size="4.6">
      <text x="42" y="194">En: Water, Mustard Seeds, Alcohol</text>
      <text x="42" y="202">Vinegar, Salt, Acidifier: Citric Acid,</text>
      <text x="42" y="210">Preservative: E224 (Sulfites).</text>
    </g>
    <line class="rule" x1="42" y1="222" x2="160" y2="222"/>
    <text class="serif ink" x="42" y="234" font-size="4.6">Ar:</text>
    <g class="arabic ink" font-size="4.8" text-anchor="end" direction="rtl">
      <text x="160" y="234">ماء ، بذور الخردل ، خل الكحول ،</text>
      <text x="160" y="242">الملح ، محمض: حمض الستريك ،</text>
      <text x="160" y="250">مواد حافظة: E224</text>
    </g>
    <line class="rule" x1="42" y1="262" x2="160" y2="262"/>
    <g class="serif red" font-size="5.4">
      <text x="42" y="275">Conditioned by Sarl Velomira/</text>
      <text x="42" y="284">conditionné par Sarl Velomira</text>
    </g>
    <text class="serif ink" x="280" y="280" font-size="6" text-anchor="end">295g/ 250ml</text>

    <!-- Nutrition facts -->
    <g class="nutrition">
      <rect class="nf-box" x="174" y="42" width="106" height="153"/>
      <text class="serif nf-text" x="178" y="53" font-size="6.2" letter-spacing="0.6">NUTRITION FACTS</text>
      <line class="nf-rule--thick" x1="177" y1="57" x2="277" y2="57"/>
      <g class="sans nf-text" font-size="3.9">
        <text x="178" y="63">10 servings per container</text>
        <text x="178" y="68">Serving size 1 tea-stick (1.2gr)</text>
      </g>
      <line class="nf-rule" x1="177" y1="72" x2="277" y2="72"/>
      <text class="sans nf-text" x="178" y="79" font-size="3.9">Amount per Serving</text>
      <text class="sans nf-text" x="276" y="88" font-size="5" text-anchor="end">0</text>
      <line class="nf-rule--thick" x1="177" y1="92" x2="277" y2="92"/>
      <text class="sans nf-text" x="276" y="99" font-size="3.6" text-anchor="end">% Daily Value*</text>
      <line class="nf-rule" x1="177" y1="102" x2="277" y2="102"/>

      <g class="sans nf-text" font-size="4.4">
        <text x="178" y="109">Total Fat 0g</text><text x="276" y="109" text-anchor="end">0%</text>
        <text x="184" y="117" font-size="3.8">Saturated Fat 0g</text><text x="276" y="117" text-anchor="end">0%</text>
        <text x="184" y="125" font-size="3.8">Trans Fat 0g</text>
        <text x="178" y="133">Cholestrol 0mg</text><text x="276" y="133" text-anchor="end">0%</text>
        <text x="178" y="141">Sodium 0g</text><text x="276" y="141" text-anchor="end">0%</text>
        <text x="178" y="149">Total Carbohydrate 0g</text><text x="276" y="149" text-anchor="end">0%</text>
        <text x="184" y="157" font-size="3.8">Dietary Fiber 0g</text><text x="276" y="157" text-anchor="end">0%</text>
        <text x="184" y="165" font-size="3.8">Total Sugars 0g</text>
        <text x="190" y="173" font-size="3.8">Includes 0g Added</text><text x="276" y="173" text-anchor="end">0%</text>
        <text x="190" y="179" font-size="3.8">Sugars</text>
      </g>
      <line class="nf-rule" x1="177" y1="112" x2="277" y2="112"/>
      <line class="nf-rule" x1="183" y1="120" x2="277" y2="120"/>
      <line class="nf-rule" x1="183" y1="128" x2="277" y2="128"/>
      <line class="nf-rule" x1="177" y1="136" x2="277" y2="136"/>
      <line class="nf-rule" x1="177" y1="144" x2="277" y2="144"/>
      <line class="nf-rule" x1="177" y1="152" x2="277" y2="152"/>
      <line class="nf-rule" x1="183" y1="160" x2="277" y2="160"/>
      <line class="nf-rule" x1="183" y1="168" x2="277" y2="168"/>
    </g>
  </svg>

  <div class="caption caption--front">FRONT</div>
  <div class="caption caption--back">BACK</div>

</main>
</body>
</html>
```